Fitness Equipment & Service

I want to make the card eye catching and fun. We are called Copperleaf Motion Limited and we are based in Wales. We sell, install and service all types of fitness equipment from Skipping ropes, right through the Dumbbells, Kettle bells and Barbells through to state of the art Treadmills, Running Machines and Strength Equipment. We also design and install changing room furniture and lockers.

TYPOGRAPHY
We would like to use Futrura. Futura has an appearance of efficiency and forwardness. The typeface is derived
from simple geometric forms (near-perfect circles, triangles and squares) and is based on strokes of
near-even weight, which are low in contrast. This is most visible in the almost perfectly round stroke of
the o, which is nonetheless slightly ovoid.
The lowercase has tall ascenders, which rise above the cap line. The uppercase
characters present proportions similar to those of classical Roman capitals.

TYPOGRAPHIC CONSIDERATIONS
No Strike though
No Horizontal Scaling
No Drop Shadows
No Effects
Never use less than 120% Leading

OUR CORPORATE COLOURS
BRAND GUIDELINES
We were thinking that our primary colour palette consists of the Acid Green (Pantone 382) and Process Black.

We work closely with torvane Ltd and would like to include their name on the card somewhere. I have attached images of the other brands that we work with as an idea or the small icons I have included that illustrate what we do?. I have very kindly been given permission to use any of the images off the files that I have included below, so I hope these help. I will include these below. I would be open to suggestions if it made the card more striking Can you do it?

Hi All, Just wanted to add a few thoughts but you are the guys with the creative visions (thats why are here) We are based in Wales, UK and we would be open to lots of different ideas on a theme but must be eye catching, Bold and FUN. If you can or think that the Welsh or any dragon could be put in there then go for it (its not a must have) We have also added some ideas for colour but again its over to you!! GO FOR IT ! Thanks and look forward to your visions! Owen

Hi All, Just thought I would sen through the contact details that need to be on the card. (if you want to play around with icons instead of the wording twitter, Facebook, go for it): Copperleaf Motion Limited Owen Pritchard Managing Director Mob: +44 (0)7391 508 262 e-mail: sales@copperleafmotion.co.uk Web: Copperleafmotion.co.uk twitter: @motionParcelbin Facebook: Copperleaf Motion Limited

```html
<!DOCTYPE html>
<html lang="en">
<head>
<meta charset="utf-8">
<title>Copperleaf Motion Limited – Business Card</title>
<link rel="stylesheet" href="https://fonts.googleapis.com/css2?family=Arimo:wght@400;700&display=swap">
<style>
  :root {
    --page-bg: #e9e7e3;
    --navy-deep: #142761;
    --navy-mid: #223f8e;
    --navy-light: #2f55b0;
    --gold: #c9a24a;
    --card-white: #ffffff;
    --card-grey: #e4e4e6;
    --ink: #1a2146;
    --ink-soft: #5a5e6e;
    --text-light: #ffffff;
  }
  * { box-sizing: border-box; margin: 0; padding: 0; }
  html, body {
    width: 1200px; height: 950px; overflow: hidden;
    background: var(--page-bg);
    font-family: "Arimo", Arial, sans-serif;
  }
  .sheet {
    width: 1200px; height: 950px;
    display: flex; flex-direction: column;
    align-items: center; justify-content: center; gap: 50px;
  }
  .card {
    width: 700px; height: 400px;
    box-shadow: 0 6px 18px rgba(0,0,0,.18);
    position: relative; overflow: hidden;
  }

  /* Front */
  .card-front { display: flex; background: var(--card-white); }
  .contact-panel {
    width: 350px; height: 100%;
    background: radial-gradient(circle at 40% 20%, var(--navy-light) 0%, var(--navy-mid) 40%, var(--navy-deep) 100%);
    color: var(--text-light);
    padding: 44px 30px 0 36px;
    border-right: 4px solid var(--gold);
  }
  .person-name { font-weight: 700; font-size: 24px; line-height: 1.2; }
  .person-role { font-size: 17px; line-height: 1.3; margin-bottom: 40px; }
  .address { font-size: 16px; line-height: 1.3; margin-bottom: 8px; }
  .contact-list { list-style: none; font-size: 16px; line-height: 1.35; }
  .contact-list li { display: flex; align-items: center; gap: 8px; }
  .contact-icon { width: 14px; height: 14px; flex: none; }

  .brand-panel {
    flex: 1; display: flex; flex-direction: column;
    align-items: center; justify-content: center; gap: 22px;
    background: linear-gradient(160deg, var(--card-white) 0%, var(--card-grey) 100%);
  }
  .brand-disc {
    width: 130px; height: 130px; border-radius: 50%;
    background: radial-gradient(circle at 40% 35%, var(--navy-light), var(--navy-deep));
  }
  .brand-name {
    font-size: 22px; font-weight: 700; color: var(--ink);
    line-height: 1.2; text-align: center;
  }

  /* Back */
  .card-back {
    background: linear-gradient(160deg, var(--card-white) 0%, var(--card-grey) 100%);
    display: flex; flex-direction: column;
    align-items: center; justify-content: center; gap: 24px;
  }
  .web-line { display: flex; align-items: center; gap: 12px; }
  .web-address { font-size: 16px; color: var(--ink-soft); line-height: 1.2; letter-spacing: .5px; }
  .web-rule { width: 60px; height: 1px; background: var(--ink); }
</style>
</head>
<body>
<main class="sheet">

  <section class="card card-front" aria-label="Business card front">
    <div class="contact-panel">
      <p class="person-name">Owen Pritchard</p>
      <p class="person-role">Managing Director</p>
      <p class="address">4172 Alderbrook Lane<br>Cedar Vale, NY 11420</p>
      <ul class="contact-list">
        <li>
          <svg class="contact-icon" viewBox="0 0 14 14" aria-hidden="true"><rect x="3.5" y="0.5" width="7" height="13" rx="1.5" fill="none" stroke="#fff" stroke-width="1.4"/><circle cx="7" cy="11" r="0.9" fill="#fff"/></svg>
          +44 (0)7391 508 262
        </li>
        <li>
          <svg class="contact-icon" viewBox="0 0 14 14" aria-hidden="true"><rect x="0.5" y="2.5" width="13" height="9" fill="#fff"/><path d="M0.5 2.5 L7 8 L13.5 2.5" fill="none" stroke="#223f8e" stroke-width="1.2"/></svg>
          sales@copperleafmotion.co.uk
        </li>
        <li>
          <svg class="contact-icon" viewBox="0 0 14 14" aria-hidden="true"><circle cx="7" cy="7" r="6" fill="none" stroke="#fff" stroke-width="1.4"/><ellipse cx="7" cy="7" rx="2.6" ry="6" fill="none" stroke="#fff" stroke-width="1"/><line x1="1" y1="7" x2="13" y2="7" stroke="#fff" stroke-width="1"/></svg>
          Copperleafmotion.co.uk
        </li>
        <li>
          <svg class="contact-icon" viewBox="0 0 14 14" aria-hidden="true"><circle cx="7" cy="7" r="6.5" fill="#fff"/></svg>
          @motionParcelbin
        </li>
        <li>
          <svg class="contact-icon" viewBox="0 0 14 14" aria-hidden="true"><rect x="0.5" y="0.5" width="13" height="13" rx="1.5" fill="#fff"/></svg>
          Copperleaf Motion Limited
        </li>
      </ul>
    </div>
    <div class="brand-panel">
      <div class="brand-disc" aria-hidden="true"></div>
      <p class="brand-name">Copperleaf Motion Limited</p>
    </div>
  </section>

  <section class="card card-back" aria-label="Business card back">
    <div class="brand-disc" aria-hidden="true"></div>
    <div class="web-line">
      <span class="web-address">copperleafmotion.co.uk</span>
      <span class="web-rule" aria-hidden="true"></span>
    </div>
  </section>

</main>
</body>
</html>
```